Mortgage Company Website / based from Moreno design

Mortgage company needs a WordPress site designed and developed using Pixel Harbor's Moreno framework. Existing site is BrellaMortgage.example.

Goals of website:
1) Attract new leads for Home loans (first-time home buyers, people moving to Dallas, and people re-financing their homes.
2) Attract and recruit new Loan Officers.

LOAN PRODUCTS OFFERED
Conventional
Jumbo
VA
FHA
USDA
Refinance
Construction Loans - not a main product. Don't like to do these.
Remodel

Target Market(s)

Middle to upper income families in the Dallas area.

Industry/Entity Type

Mortgage Brokerage

Coding

Coded - Design and coding required

Number of Pages Required

2 page

Requirements
Must have
• Must use one of the Moreno theme from Pixel Harbor for development
https://moreno.pixelharbor.example/

Client is focused on higher-end clientele and likes the use of the color gold.

NAVIGATION
Home Loans
Mortgage Resources
About Us
Contact Us

Site must also look good on mobile phones and tablets. Moreno theme has breakpoints already developed so should make that easier.
Nice to have
• Client likes the designs of these sites:
https://quenby.example/home-loans (this one was talked about as her favorite)
https://thewardlowpartners.example/
https://www.harborlinelending.example/

- Overall wants the site to be clean with lots of white space

Wants to keep the imagery focused on the families and people buying the home.

Also likes the focus on giving back to the community from the example site provided. Brella gives to "Hands for Tails"

Things that can be featured on the home page:
* Hero image on top
* Top of Z, Veltrix Market Leader award. Veltrix 100 Mortgage Market Leader 2020
* 3 Most recent blog posts
* Video from current homepage
* Get started form: Name, Email, Phone. Submit button
* Footer area can have navigation, contact info, and awards sections

some possible Moreno templates to choose from:
https://moreno.pixelharbor.example/charity/
https://moreno.pixelharbor.example/cryptocurrency/
https://moreno.pixelharbor.example/freelancer/
https://moreno.pixelharbor.example/finance/
https://moreno.pixelharbor.example/financial-advisor/
https://moreno.pixelharbor.example/university/
https://moreno.pixelharbor.example/marketing-consultant/

```html
<!DOCTYPE html>
<html lang="en">
<head>
<meta charset="utf-8">
<title>Brella Mortgage Inc.</title>
<link rel="stylesheet" href="https://fonts.googleapis.com/css2?family=Montserrat:wght@400;500;600;700&display=swap">
<style>
:root{
  --gold:#c9a73a;
  --ink:#1d1d1d;
  --text:#6b6b6b;
  --soft:#f6f6f6;
  --line:#e4e4e4;
  --footer:#1f1f1f;
  --white:#ffffff;
}
*{box-sizing:border-box;margin:0;padding:0}
html,body{width:1200px;height:3759px;overflow:hidden}
body{font-family:"Montserrat",sans-serif;color:var(--ink);background:var(--white);position:relative}
section,header,footer{position:relative;width:1200px}

/* header */
.site-header{height:93px;background:var(--white)}
.brand{position:absolute;left:127px;top:16px;text-align:center}
.brand-name{font-weight:700;font-size:44px;letter-spacing:1px;line-height:46px;color:var(--ink)}
.brand-sub{font-size:7px;font-weight:600;letter-spacing:2px;color:var(--ink)}
.main-nav{position:absolute;left:394px;top:0;display:flex;height:93px;align-items:center}
.main-nav a{font-size:13.5px;color:#333;text-decoration:none;padding:0 14px;height:93px;line-height:93px}
.main-nav a.active{color:var(--gold);background:#f7f7f7;padding:0 16px}
.btn-start{position:absolute;left:946px;top:27px;width:128px;height:40px;background:var(--ink);color:var(--white);font-size:14px;font-weight:500;display:flex;align-items:center;justify-content:center;border-radius:2px}

/* hero */
.hero{height:506px;overflow:hidden;
  background:
    radial-gradient(ellipse 260px 230px at 250px 330px,#a08a5c 0%,#8d7a4f 45%,rgba(141,122,79,0) 100%),
    radial-gradient(ellipse 200px 200px at 870px 330px,#e9e6e0 0%,#d4cfc5 50%,rgba(212,207,197,0) 100%),
    linear-gradient(180deg,rgba(0,0,0,0) 70%,#5e5446 100%),
    radial-gradient(circle at 80% 20%,#c88a73 0%,rgba(200,138,115,0) 25%),
    linear-gradient(110deg,#3f5a2c 0%,#5d7a3c 35%,#7b8c55 60%,#4f6a34 100%)}
.hero::after{content:"";position:absolute;inset:0;background:rgba(0,0,0,.18)}
.hero-caption{position:absolute;left:0;right:0;top:180px;text-align:center;color:var(--white);z-index:1}
.hero-caption h1{font-size:28px;font-weight:500;line-height:33px;text-shadow:0 1px 6px rgba(0,0,0,.35)}
.btn-gold{display:inline-block;background:var(--gold);color:var(--ink);font-size:12.5px;font-weight:500;padding:8px 20px;border-radius:2px}
.hero-caption .btn-gold{margin-top:20px}
.dots{display:flex;gap:10px;justify-content:center}
.dots span{width:9px;height:9px;border-radius:50%;border:1.5px solid #bbb}
.dots span.on{background:var(--gold);border-color:var(--gold)}
.hero .dots{position:absolute;left:0;right:0;top:564px;top:564px;top:565px}
.hero .dots{top:565px;top:565px}
.hero .dots{top:565px}
.hero .dots{top:565px}

/* section titles */
.sec-title{text-align:center;color:var(--gold);font-size:20px;font-weight:600;letter-spacing:.5px;display:flex;align-items:center;justify-content:center;gap:12px}
.sec-title::before,.sec-title::after{content:"";width:20px;height:2px;background:var(--gold)}

/* loan products */
.products{height:665px}
.products .sec-title{position:absolute;left:0;right:0;top:52px}
.card-grid{position:absolute;left:127px;top:115px;display:grid;grid-template-columns:repeat(3,300px);column-gap:23px;row-gap:29px}
.product-card{height:146px;background:var(--white);box-shadow:0 2px 10px rgba(0,0,0,.09);padding:28px 24px 0;position:relative}
.product-card .num{position:absolute;right:24px;top:-2px;width:35px;height:32px;background:var(--gold);color:var(--white);font-size:17px;font-weight:500;display:flex;align-items:center;justify-content:center}
.product-card h3{font-size:18.5px;font-weight:600;margin-bottom:10px}
.product-card p{font-size:12.2px;line-height:19px;color:var(--text);width:245px}
.view-all{display:flex;align-items:center;justify-content:center;font-size:16px;color:var(--text);gap:10px;padding:0}

/* team */
.resources{height:402px;background:var(--soft)}
.resources .sec-title{position:absolute;left:0;right:0;top:50px}
.team{position:absolute;left:127px;top:106px;display:flex;gap:24px}
.member{width:218px;text-align:center}
.member .frame{background:var(--white);padding:5px;box-shadow:0 1px 6px rgba(0,0,0,.12);height:222px}
.photo{width:100%;height:100%}
.photo.p1{background:radial-gradient(ellipse 70px 80px at 50% 42%,#b88a72 0%,rgba(184,138,114,0) 100%),radial-gradient(ellipse 110px 70px at 50% 100%,#4a5878 0%,#4a5878 60%,rgba(74,88,120,0) 100%),linear-gradient(90deg,#2f6b36 0%,#4f8e46 50%,#a8a89a 100%)}
.photo.p2{background:radial-gradient(ellipse 70px 90px at 50% 35%,#6a5a52 0%,rgba(106,90,82,0) 100%),#474442;display:flex;flex-direction:column;justify-content:center;align-items:center;color:var(--white);font-size:13px;line-height:17px;padding:40px 14px 0}
.photo.p3{background:radial-gradient(ellipse 70px 85px at 50% 40%,#c49a80 0%,rgba(196,154,128,0) 100%),radial-gradient(ellipse 110px 60px at 50% 100%,#222 0%,rgba(34,34,34,0) 100%),linear-gradient(160deg,#2d3a2a,#6b6b5a)}
.photo.p4{background:radial-gradient(ellipse 70px 85px at 50% 40%,#c29276 0%,rgba(194,146,118,0) 100%),radial-gradient(ellipse 110px 70px at 50% 100%,#2a2a2a 0%,rgba(42,42,42,0) 100%),linear-gradient(160deg,#f1f1f1,#d9d9d9)}
.social{display:flex;gap:12px;margin-top:14px}
.social span{width:24px;height:24px;border-radius:50%;background:var(--white)}
.social span.gold{background:var(--gold)}
.member h4{font-size:14px;font-weight:600;margin-top:14px}

/* about */
.about{height:548px}
.about .sec-title{position:absolute;left:0;right:0;top:52px}
.about-media{position:absolute;left:127px;top:104px;width:445px;height:403px;background:#f1f1f1;padding:12px 15px 17px 15px}
.about-media .img{width:100%;height:100%;position:relative;
  background:
    radial-gradient(ellipse 120px 110px at 30% 55%,#c58a72 0%,rgba(197,138,114,0) 100%),
    radial-gradient(ellipse 120px 110px at 70% 60%,#d6846e 0%,rgba(214,132,110,0) 100%),
    linear-gradient(180deg,#e7ddd0 0%,#d9c4ad 45%,#ece9e4 80%,#f5f3ef 100%)}
.play{position:absolute;right:6px;bottom:6px;width:70px;height:70px;background:var(--gold);display:flex;align-items:center;justify-content:center}
.about-text{position:absolute;left:612px;top:126px;width:440px}
.about-text h3{font-size:15.5px;font-weight:600;line-height:23px;margin-bottom:23px}
.about-text p{font-size:13.6px;line-height:24px;color:#444;margin-bottom:23px}
.about-text .btn-gold{margin-top:7px;padding:9px 20px}

/* blogs */
.blogs{height:438px;background:var(--soft)}
.blogs .sec-title{position:absolute;left:0;right:0;top:52px}
.blog-grid{position:absolute;left:127px;top:109px;display:grid;grid-template-columns:repeat(3,300px);column-gap:23px}
.blog-img{height:183px}
.b1{background:radial-gradient(ellipse 90px 70px at 40% 45%,#c59a80 0%,rgba(197,154,128,0) 100%),linear-gradient(135deg,#6e5240,#b99b84 55%,#e4ddd5)}
.b2{background:radial-gradient(ellipse 60px 50px at 40% 40%,#3a3a3a 0%,rgba(58,58,58,0) 100%),radial-gradient(ellipse 50px 25px at 62% 72%,#d9a3a3 0%,rgba(217,163,163,0) 100%),#f1f1f1}
.b3{background:radial-gradient(ellipse 60px 50px at 55% 70%,#f2e8dc 0%,rgba(242,232,220,0) 100%),linear-gradient(135deg,#e0a04a 0%,#8a8a3a 50%,#3f5a26 100%)}
.blog h4{font-size:14.5px;font-weight:500;line-height:19px;margin-top:21px}
.blog-meta{display:flex;align-items:center;margin-top:20px;font-size:11.5px;color:#444}
.blog-meta svg{margin-right:7px}
.btn-line{margin-left:25px;border:1px solid #bbb;font-size:11.5px;padding:5px 19px;background:var(--white);color:var(--ink)}
.btn-line.fill{background:var(--gold);border-color:var(--gold)}

/* testimonials */
.testimonials{height:716px}
.testimonials .sec-title{position:absolute;left:0;right:0;top:52px}
.quote-mark{position:absolute;left:566px;top:98px;width:68px;height:68px;border-radius:50%;background:#ebebeb;display:flex;align-items:center;justify-content:center}
.quote{position:absolute;left:220px;width:760px;top:186px;text-align:center;font-size:13.4px;line-height:20px;color:#333}
.quote-meta{position:absolute;left:0;right:0;top:266px;display:flex;justify-content:center;align-items:center;font-size:12px;color:#444}
.quote-meta .sep{width:1px;height:14px;background:#bbb;margin:0 12px}
.quote-meta b{font-weight:600;color:var(--ink)}
.testimonials .dots{position:absolute;left:0;right:0;top:312px}
.form-card{position:absolute;left:190px;top:385px;width:820px;height:372px;background:var(--white);box-shadow:0 2px 14px rgba(0,0,0,.12);display:flex;z-index:2}
.form-side{width:426px;padding:24px 30px;border-right:3px solid var(--gold)}
.form-side h3{font-size:20px;font-weight:500;color:var(--gold);margin-bottom:18px}
.field{height:38px;border:1px solid var(--line);font-size:13px;color:#999;padding:10px 14px;margin-bottom:15px;width:364px}
.field.msg{height:70px}
.btn-submit{display:inline-block;background:var(--gold);color:var(--white);font-size:12px;font-weight:600;padding:9px 24px;margin-top:8px}
.map{flex:1;position:relative;background:radial-gradient(circle at 45% 52%,#f4efe6 0%,rgba(244,239,230,0) 40%),linear-gradient(135deg,#eeefea,#e3e7e1)}
.map svg{position:absolute;left:172px;top:188px}

/* footer */
.site-footer{position:absolute;top:3368px;left:0;width:1200px;height:391px;background:var(--footer);color:var(--white)}
.f-brand{position:absolute;left:127px;top:92px;text-align:center}
.f-brand .brand-name{color:var(--white);font-size:40px;line-height:42px}
.f-brand .brand-sub{color:var(--white)}
.f-about{position:absolute;left:127px;top:200px;font-size:12.5px;line-height:19px;width:210px}
.f-social{position:absolute;left:127px;top:262px;display:flex;gap:14px}
.f-social span{width:24px;height:24px;border-radius:50%;background:var(--white)}
.f-social span.gold{background:var(--gold)}
.f-col{position:absolute;top:100px}
.f-col h4{color:var(--gold);font-size:18px;font-weight:600;margin-bottom:22px;line-height:21px}
.f-links{left:384px}
.f-links li{list-style:none;font-size:12.5px;margin-bottom:13px}
.f-links li::before{content:"→";margin-right:8px;font-size:11px}
.f-links li.active{color:var(--gold)}
.f-contact{left:582px}
.c-row{display:flex;gap:14px;font-size:12.5px;line-height:19px;margin-bottom:18px}
.c-row svg{flex:none;margin-top:2px}
.f-award{left:857px}
.badges{display:flex;gap:12px}
.badge{width:44px;height:72px;background:#d11f2a;border:3px solid var(--white)}
.yt-box{margin-top:24px;width:204px;height:52px;background:#2d2d2d;display:flex;align-items:center;justify-content:space-between;padding:0 14px;font-size:12.5px;line-height:16px}
.yt-box i{width:34px;height:24px;background:#e12a2a;border-radius:5px}
.copyright{position:absolute;left:0;right:0;bottom:0;height:41px;background:var(--gold);color:#333;font-size:12.5px;display:flex;align-items:center;justify-content:center}
</style>
</head>
<body>

<header class="site-header">
  <div class="brand"><div class="brand-name">BRELLA</div><div class="brand-sub">MORTGAGE INC</div></div>
  <nav class="main-nav">
    <a class="active">Home Loans</a><a>Mortgage Resources</a><a>About Us</a><a>Blogs</a><a>Contact Us</a>
  </nav>
  <div class="btn-start">Get Started</div>
</header>

<section class="hero" role="img" aria-label="Photo of a loan money sack and a small model house balanced on a seesaw against a green garden">
  <div class="hero-caption">
    <h1>Lowest Interest Rate on<br>Home Loan</h1>
    <span class="btn-gold">Read More</span>
  </div>
</section>
<div class="dots" style="position:absolute;left:0;right:0;top:565px;z-index:2"><span style="border-color:#fff"></span><span class="on"></span><span style="border-color:#fff"></span></div>

<section class="products">
  <h2 class="sec-title">LOAN PRODUCTS</h2>
  <div class="card-grid">
    <div class="product-card"><span class="num">01</span><h3>Conventional</h3><p>Lorem Ipsum is simply dummy text of the printing and typesetting industry. industry's...</p></div>
    <div class="product-card"><span class="num">02</span><h3>Jumbo</h3><p>Lorem Ipsum is simply dummy text of the printing and typesetting industry. industry's...</p></div>
    <div class="product-card"><span class="num">03</span><h3>VA</h3><p>Lorem Ipsum is simply dummy text of the printing and typesetting industry. industry's...</p></div>
    <div class="product-card"><span class="num">04</span><h3>FHA</h3><p>Lorem Ipsum is simply dummy text of the printing and typesetting industry. industry's...</p></div>
    <div class="product-card"><span class="num">05</span><h3>USDA</h3><p>Lorem Ipsum is simply dummy text of the printing and typesetting industry. industry's...</p></div>
    <div class="product-card"><span class="num">06</span><h3>Refinance</h3><p>Lorem Ipsum is simply dummy text of the printing and typesetting industry. industry's...</p></div>
    <div class="product-card"><span class="num">07</span><h3>Construction Loans</h3><p>Lorem Ipsum is simply dummy text of the printing and typesetting industry. industry's...</p></div>
    <div class="product-card"><span class="num">08</span><h3>Remodel</h3><p>Lorem Ipsum is simply dummy text of the printing and typesetting industry. industry's...</p></div>
    <div class="product-card view-all">View All
      <svg width="14" height="12" viewBox="0 0 14 12"><path d="M1 6h11M7 1l5 5-5 5" fill="none" stroke="#333" stroke-width="1.8"/></svg>
    </div>
  </div>
</section>

<section class="resources">
  <h2 class="sec-title">MORTGAGE RESOURCES</h2>
  <div class="team">
    <div class="member"><div class="frame"><div class="photo p1" role="img" aria-label="Portrait of loan officer Daniel Hartwell in a suit against a green wall"></div></div><h4>Daniel Hartwell</h4></div>
    <div class="member"><div class="frame"><div class="photo p2" role="img" aria-label="Portrait of loan officer Lauren Pell with hover overlay">Lorem Ipsum is simply dummy text of the printing and typesetting...<div class="social"><span></span><span></span><span class="gold"></span><span></span></div></div></div><h4>Lauren Pell</h4></div>
    <div class="member"><div class="frame"><div class="photo p3" role="img" aria-label="Portrait of loan officer Grace Lin Porter outdoors"></div></div><h4>Grace Lin Porter</h4></div>
    <div class="member"><div class="frame"><div class="photo p4" role="img" aria-label="Portrait of loan officer Rosa Alvarado on a light background"></div></div><h4>Rosa Alvarado</h4></div>
  </div>
</section>

<section class="about">
  <h2 class="sec-title">ABOUT US</h2>
  <div class="about-media">
    <div class="img" role="img" aria-label="Video still of a young couple on a rug looking at a laptop among moving boxes">
      <div class="play"><svg width="30" height="34" viewBox="0 0 30 34"><path d="M4 3l23 14L4 31z" fill="none" stroke="#1d1d1d" stroke-width="2.5" stroke-linejoin="round"/></svg></div>
    </div>
  </div>
  <div class="about-text">
    <h3>BRELLA Mortgage Inc. is a residential<br>mortgage company.</h3>
    <p>BRELLA stands for Integrity, Knowledge of the market and products, Outstanding service, and New and better ways of helping our cliental. The company was founded with the core value of giving, honesty, efficiency, humanity, and doing business with integrity.</p>
    <p>We not only believe in working hard for our clients, but also working efficiently with expertise to deliver results...</p>
    <span class="btn-gold">Read More</span>
  </div>
</section>

<section class="blogs">
  <h2 class="sec-title">BLOGS</h2>
  <div class="blog-grid">
    <article class="blog"><div class="blog-img b1" role="img" aria-label="Couple reviewing paperwork at a kitchen table"></div><h4>Lorem Ipsum is simply dummy text of the printing and typesetting...</h4>
      <div class="blog-meta"><svg width="14" height="14" viewBox="0 0 14 14"><rect x="1" y="2" width="12" height="11" rx="1" fill="none" stroke="#c9a73a" stroke-width="1.3"/><path d="M1 5h12M4 0v3M10 0v3" stroke="#c9a73a" stroke-width="1.3"/></svg>30 Nov, 2020<span class="btn-line fill">Read More</span></div></article>
    <article class="blog"><div class="blog-img b2" role="img" aria-label="Rubber stamp beside an approved loan stamp mark"></div><h4>Lorem Ipsum is simply dummy text of the printing and typesetting...</h4>
      <div class="blog-meta"><svg width="14" height="14" viewBox="0 0 14 14"><rect x="1" y="2" width="12" height="11" rx="1" fill="none" stroke="#c9a73a" stroke-width="1.3"/><path d="M1 5h12M4 0v3M10 0v3" stroke="#c9a73a" stroke-width="1.3"/></svg>30 Nov, 2020<span class="btn-line">Read More</span></div></article>
    <article class="blog"><div class="blog-img b3" role="img" aria-label="Hand holding a small model house with a money bag above"></div><h4>Lorem Ipsum is simply dummy text of the printing and typesetting...</h4>
      <div class="blog-meta"><svg width="14" height="14" viewBox="0 0 14 14"><rect x="1" y="2" width="12" height="11" rx="1" fill="none" stroke="#c9a73a" stroke-width="1.3"/><path d="M1 5h12M4 0v3M10 0v3" stroke="#c9a73a" stroke-width="1.3"/></svg>30 Nov, 2020<span class="btn-line">Read More</span></div></article>
  </div>
</section>

<section class="testimonials">
  <h2 class="sec-title">TESTIMONIALS</h2>
  <div class="quote-mark"><svg width="34" height="26" viewBox="0 0 34 26"><path d="M2 26V14C2 6 6 2 14 0v5c-4 1-6 4-6 8h6v13zM20 26V14c0-8 4-12 12-14v5c-4 1-6 4-6 8h6v13z" fill="#c9a73a"/></svg></div>
  <p class="quote">We have worked with Dan Hartwell and the BRELLA Mortgage team several times and every time has been incredibly pleasant! They genuinely care about their clients and communicate very well to make it a smooth process from start to finish. Give them a call if you need to buy a house or refinance your current one!!</p>
  <div class="quote-meta"><svg width="14" height="14" viewBox="0 0 14 14" style="margin-right:7px"><rect x="1" y="2" width="12" height="11" rx="1" fill="none" stroke="#c9a73a" stroke-width="1.3"/><path d="M1 5h12M4 0v3M10 0v3" stroke="#c9a73a" stroke-width="1.3"/></svg>30 Nov, 2020<span class="sep"></span><b>Megan Rhodes</b></div>
  <div class="dots"><span></span><span class="on"></span><span></span></div>

  <div class="form-card">
    <div class="form-side">
      <h3>Get started form</h3>
      <div class="field">Name</div>
      <div class="field">Email</div>
      <div class="field">Phone</div>
      <div class="field msg">Message</div>
      <span class="btn-submit">SUBMIT</span>
    </div>
    <div class="map" role="img" aria-label="Street map showing the Brella Mortgage office location in Dallas">
      <svg width="22" height="30" viewBox="0 0 22 30"><path d="M11 0a11 11 0 0 0-11 11c0 8 11 19 11 19s11-11 11-19A11 11 0 0 0 11 0z" fill="#e53935"/><circle cx="11" cy="11" r="4" fill="#8e1b1b"/></svg>
    </div>
  </div>
</section>

<footer class="site-footer">
  <div class="f-brand"><div class="brand-name">BRELLA</div><div class="brand-sub">MORTGAGE INC</div></div>
  <p class="f-about">Lorem Ipsum is simply dummy text of the printing and...</p>
  <div class="f-social"><span></span><span></span><span class="gold"></span><span></span></div>

  <div class="f-col f-links"><h4>Quick Link</h4>
    <ul><li class="active">Home Loans</li><li>Mortgage Resources</li><li>About Us</li><li>Blogs</li><li>Contact Us</li><li>Privacy &amp; Disclaimer</li></ul>
  </div>

  <div class="f-col f-contact"><h4>Conatct info</h4>
    <div class="c-row"><svg width="16" height="20" viewBox="0 0 16 20"><path d="M8 0a8 8 0 0 0-8 8c0 6 8 12 8 12s8-6 8-12a8 8 0 0 0-8-8zm0 11a3 3 0 1 1 0-6 3 3 0 0 1 0 6z" fill="#fff"/></svg><span>4820 Linden Avenue, Suite 310<br>Dallas, TX 75240</span></div>
    <div class="c-row"><svg width="16" height="16" viewBox="0 0 16 16"><path d="M3 0l3 4-2 2c1 2 4 5 6 6l2-2 4 3-2 3C7 16 0 9 0 3z" fill="#fff"/></svg><span>214-555-0142</span></div>
    <div class="c-row"><svg width="16" height="16" viewBox="0 0 16 16"><rect x="4" y="0" width="8" height="4" fill="#fff"/><rect x="0" y="5" width="16" height="7" rx="1" fill="#fff"/><rect x="4" y="10" width="8" height="6" fill="#fff" stroke="#1f1f1f"/></svg><span>1-800-555-0199</span></div>
    <div class="c-row"><svg width="16" height="13" viewBox="0 0 16 13"><rect width="16" height="13" fill="#fff"/><path d="M0 0l8 7 8-7M0 13l6-6M16 13l-6-6" stroke="#1f1f1f" stroke-width="1.2" fill="none"/></svg><span>info@brellamortgage.example</span></div>
  </div>

  <div class="f-col f-award"><h4>The Peoples Lender!<br>We Make It Happen.</h4>
    <div class="badges"><span class="badge" role="img" aria-label="Top of Z award 2017"></span><span class="badge" role="img" aria-label="Top of Z award 2014"></span></div>
    <div class="yt-box"><span>BRELLA Mortgage<br>Has your back!</span><i></i></div>
  </div>

  <div class="copyright">Copyright © 2020 Brella Mortgage Inc. All Rights Reserved</div>
</footer>

</body>
</html>
```